Healthy Products Company Needs to Refresh Their Web Image

This is a web relaunch for a company that creates a nutritional supplement made out of Greenlipped Mussels that are native to and grow only in New Zealand. This product is a health superfood which is excellent support for many conditions such as arthritis, heart disease, joint mobility, and healthy lung function, etc. Trevolin Marine is a pioneer in this industry having started in 1967. They have pioneered and are the only company in the business to use cool drying methodology to dry their mussels. This low heat process doesn't degrade nutritional and health giving properties of the mussels. The final design should communicate, cool, healthy, green and natural feeling superimposed on cutting edge technology, and pharmaceutical purity. Natural yet scientific. Also a certain solidity and trustworthiness.
Updates

Hi: The web site name is www.trevolin.com and I would like to have both the psd file and the underlying code.
Thank you.

Target Market(s)

Corporates: Pharmaceutical Companies, Heath Product Companies

Industry/Entity Type

Pharmaceutical

Requirements
Must have
• Currently we have no way to order the product online and we will not be doing this in the current site. However, capability to do that in the future would be nice.
Please see the previous web site for understanding of what the company does. Plese feel free to run with any ideas you may have in layout or content. I have enclosed a new logo for the company. Please make sure you carry the style of the logo throughout the new web site. I don't have any new pictures we can use right now but I will include a background picture you can use for now as a placeholder.

```html
<!DOCTYPE html>
<html lang="en">
<head>
<meta charset="utf-8">
<title>Trevolin Marine</title>
<link href="https://fonts.googleapis.com/css2?family=Fira+Sans:wght@400;500&family=Roboto+Condensed:wght@400&family=Noto+Serif:wght@400&family=Open+Sans:wght@600&display=swap" rel="stylesheet">
<style>
:root{
  --lake-top:#2f6f8a;
  --lake-mid:#3f9fd6;
  --lake-bottom:#3aa6ee;
  --page:#f6f6f6;
  --nav:#2e86e8;
  --brand-green:#0b7a3e;
  --heading-green:#0f6e3c;
  --link-blue:#2a86dd;
  --news-title:#1f7a6a;
  --news-head:#6f8aa6;
  --text:#666;
  --muted:#999;
  --rule:#ddd;
  --ink:#333;
}
*{box-sizing:border-box;margin:0;padding:0}
html,body{width:1200px;height:1113px;overflow:hidden}
body{position:relative;font-family:"Fira Sans",sans-serif;color:var(--text)}
.backdrop{position:absolute;inset:0;background:linear-gradient(180deg,var(--lake-top) 0%,#2d5a3a 20%,#2f6a4a 45%,var(--lake-mid) 62%,var(--lake-bottom) 100%)}
.page{position:absolute;left:110px;top:0;width:980px;height:1113px;background:var(--page)}
.brand{position:absolute;left:28px;top:34px;display:flex;align-items:center;gap:10px}
.brand-dot{width:20px;height:20px;border-radius:50%;background:var(--brand-green)}
.brand-name{font-size:30px;font-weight:500;color:var(--brand-green);letter-spacing:-.3px}
.contact{position:absolute;left:745px;top:32px;color:var(--brand-green)}
.contact-phone{display:flex;align-items:center;gap:6px;font-size:20px}
.contact-mail{font-size:15px;margin-top:4px}
.contact-mail a{color:var(--brand-green);text-decoration:underline}
.nav{position:absolute;left:0;top:111px;width:980px;height:46px;background:var(--nav);display:flex;align-items:center}
.nav a{position:absolute;top:16px;color:#fff;text-decoration:none;font:600 13.5px "Open Sans",sans-serif;text-shadow:0 1px 1px rgba(0,0,0,.25)}
.hero{position:absolute;left:0;top:157px;width:980px;height:364px;background:linear-gradient(90deg,#6b5a3c 0%,#3f5a2f 30%,#c9b6a4 55%,#ece8e2 75%,#d9d0c6 100%)}
.intro-box{position:absolute;left:14px;top:539px;width:714px;height:511px;border:1px solid var(--rule)}
.intro-title{position:absolute;left:13px;top:14px;width:600px;font-size:24px;line-height:26px;font-weight:400;color:var(--heading-green)}
.intro-text{position:absolute;left:15px;top:73px;width:680px;font-size:13px;line-height:18px;color:var(--text)}
.intro-text a{color:var(--ink);text-decoration:none}
.intro-rule{position:absolute;left:14px;top:155px;width:690px;border-top:1px solid var(--rule)}
.feature{position:absolute;left:13px;width:690px}
.feature-thumb{position:absolute;left:0;top:0;width:142px;height:95px;background:linear-gradient(135deg,#3a2f22,#b07a38 55%,#2e2a22)}
.feature-title{position:absolute;left:160px;top:0;font-size:18px;font-weight:400;color:var(--link-blue)}
.feature-text{position:absolute;left:160px;top:26px;width:522px;font-size:12.5px;line-height:16px;color:var(--text)}
.news{position:absolute;left:744px;top:544px;width:218px}
.news-heading{font:400 19px "Roboto Condensed",sans-serif;color:var(--news-head)}
.news-item{padding:12px 0 12px;border-bottom:1px solid var(--rule)}
.news-item:last-child{border-bottom:0}
.news-date{font:400 9px "Fira Sans",sans-serif;color:var(--muted);text-transform:uppercase;letter-spacing:.3px}
.news-title{font:400 14px/18px "Roboto Condensed",sans-serif;color:var(--news-title);margin-top:11px}
.news-text{font:400 10.5px/16px "Noto Serif",serif;color:var(--text);margin-top:6px}
.promo{position:absolute;left:742px;top:829px;width:220px;height:220px;background:linear-gradient(160deg,#c9b37c,#b89e62)}
.footer-copy{position:absolute;left:15px;top:1075px;font-size:12.5px;color:var(--ink)}
.footer-links{position:absolute;right:15px;top:1076px;display:flex;gap:15px}
.footer-links a{font-size:12.5px;color:var(--ink);text-decoration:none}
</style>
</head>
<body>
<div class="backdrop" role="img" aria-label="Lake with forested hills under blue water"></div>
<div class="page">
  <header>
    <div class="brand"><span class="brand-dot"></span><span class="brand-name">Trevolin Marine</span></div>
    <div class="contact">
      <div class="contact-phone">
        <svg width="24" height="18" viewBox="0 0 24 18"><path d="M2 6c0-3 4-4 10-4s10 1 10 4v2h-5V6c-2-.6-8-.6-10 0v2H2z" fill="#0b7a3e"/><rect x="5" y="9" width="14" height="8" rx="2" fill="#0b7a3e"/></svg>
        <span>+(640) 555-0192</span>
      </div>
      <div class="contact-mail">Email: <a href="#">Sales@trevolin.com</a></div>
    </div>
  </header>
  <nav class="nav">
    <a href="#" style="left:31px">HOME</a>
    <a href="#" style="left:135px">THE TREVOLIN STORY</a>
    <a href="#" style="left:318px">PRODUCT SPECIFICATIONS</a>
    <a href="#" style="left:553px">BACKGROUND INFO</a>
    <a href="#" style="left:744px">CONTACT US</a>
    <a href="#" style="left:890px">SITE MAP</a>
  </nav>
  <div class="hero" role="img" aria-label="Hands holding green-lipped mussels beside a smiling older couple"></div>

  <section class="intro-box">
    <h1 class="intro-title">We Provide Nutritional supplement made out of Greenlipped Mussels.</h1>
    <p class="intro-text">Le Lorem Ipsum est le faux texte standard de l'imprimerie depuis les années 1500, quand un peintre anonyme assembla ensemble. Texte pour réaliser un livre spécimen de polices de texte. Il n'a pas fait que survivre cinq siècles, mais s'est aussi adapté à la bureautique informatique., sans que son contenu n'en soit modifié. Il a été popularisé dans les années 1960. <a href="#">Read More &gt;</a></p>
    <div class="intro-rule"></div>

    <article class="feature" style="top:178px">
      <div class="feature-thumb" role="img" aria-label="Opened mussels on the half shell"></div>
      <h2 class="feature-title">Mucopolysaccharides</h2>
      <p class="feature-text">A key factor in human metabolism, growth and health is a group of complex carbohy-drates called mucopolysaccharides, (MPS). MPS are long chain amino sugars with active sulfate and amino molecules along the multiple polysaccharide chains, usually com-bined with a core protein.</p>
    </article>
    <article class="feature" style="top:290px">
      <div class="feature-thumb" role="img" aria-label="Hands holding fresh mussels" style="background:linear-gradient(135deg,#d8d2c8,#4a4436 50%,#e2c8b4)"></div>
      <h2 class="feature-title">Bioactive Nutrition from Nature</h2>
      <p class="feature-text">A key factor in human metabolism, growth and health is a group of complex carbohy-drates called mucopolysaccharides, (MPS). MPS are long chain amino sugars with active sulfate and amino molecules along the multiple polysaccharide chains, usually com-bined with a core protein.</p>
    </article>
    <article class="feature" style="top:401px">
      <div class="feature-thumb" role="img" aria-label="Rows of cooked mussels" style="background:linear-gradient(135deg,#3c3a2c,#d08a30 50%,#3a3528)"></div>
      <h2 class="feature-title">The Cradle of Life</h2>
      <p class="feature-text">A key factor in human metabolism, growth and health is a group of complex carbohy-drates called mucopolysaccharides, (MPS). MPS are long chain amino sugars with active sulfate and amino molecules along the multiple polysaccharide chains, usually com-bined with a core protein.</p>
    </article>
  </section>

  <aside class="news">
    <h3 class="news-heading">News &amp; Events</h3>
    <div class="news-item">
      <div class="news-date">Tuesday, June 25 2013</div>
      <div class="news-title">Healthy Eating on a Budget</div>
      <p class="news-text">Written by Mara Ellison, a registered dietitian at Harbourview Regional who is passionate about all things...</p>
    </div>
    <div class="news-item">
      <div class="news-date">Thursday, June 20 2013</div>
      <div class="news-title">Desmond Farrow Named Employee of the Month</div>
      <p class="news-text">Congratulations to Desmond Farrow, Sr., for being named Harbourview's employee of the month in May. As a...</p>
    </div>
  </aside>
  <div class="promo" role="img" aria-label="Promotional banner for a collagen supplement value pack"></div>

  <footer>
    <div class="footer-copy">© Copyright 2013 Website Name. All Rights Reserved.</div>
    <div class="footer-links">
      <a href="#">The Trevolin Story</a>
      <a href="#">Product Specifications</a>
      <a href="#">Background Information</a>
      <a href="#">Contact Us</a>
    </div>
  </footer>
</div>
</body>
</html>
```